TR Advisory Business Cards - High End AV / Low Voltage Company

We are low voltage AV company that specializes in high end clients on the residential side and larger businesses on the commercial side. We want something modern, tech looking but also something that is extremely professional looking. We have uploaded our logos and postcards we already have in the field. Along with a picture of one of our wrapped vans. Our website is at www.trvadvisory.example and our primary colors are the orange, green, grey and blue all military color finishes.

We are interesting in the slogans "Connecting You with Smarter Systems" or "Setting the Standard in Tech"

Target Market(s)

We focus on 70% Commercial and 30% Residential Customers

Industry/Entity Type

Low Voltage, AV Company

Contact Information for Business Card

Name - Dorian Fairweather, Title - Owner, Office Phone - 555-714-3096, Mobile Phone - 555-802-4173, E-Mail - d@trvadvisory.example, Website: www.trvadvisory.example

Font styles to use
Sans Serif

Requirements
Must have
• Must have Name, Title, Work Phone & Mobile, Website and Logo.
Nice to have
• We want something that will impress our higher end clients with a great logo
Should not have
• Too traditional or plain.

```html
<!DOCTYPE html>
<html lang="en">
<head>
<meta charset="UTF-8">
<title>TR Advisory Business Cards</title>
<link rel="stylesheet" href="https://fonts.googleapis.com/css2?family=Montserrat:wght@400;500;600;700&display=swap">
<style>
  :root {
    --page: #2a2a2a;
    --card: #0b0b0b;
    --orange: #ec6a35;
    --white: #f4f4f4;
    --silver: #c9c9c9;
    --divider: #3a3a3a;
  }
  * { box-sizing: border-box; margin: 0; padding: 0; }
  html, body {
    width: 1200px; height: 900px; overflow: hidden;
    background: var(--page);
    font-family: "Montserrat", sans-serif;
  }
  .sheet {
    width: 1200px; height: 900px;
    display: flex; flex-direction: column; align-items: center; justify-content: center;
    gap: 48px;
  }
  .card {
    position: relative;
    width: 640px; height: 366px;
    background: var(--card);
    border-radius: 26px;
    overflow: hidden;
    box-shadow: 0 12px 30px rgba(0,0,0,.45);
  }
  /* front */
  .card-front .brand {
    position: absolute; left: 40px; top: 120px; width: 250px;
    display: flex; align-items: center; gap: 14px;
  }
  .brand-dot {
    width: 34px; height: 34px; border-radius: 50%;
    border: 4px solid var(--orange); flex: none;
  }
  .brand-name {
    color: var(--orange); font-weight: 600; font-size: 31px; letter-spacing: .5px;
    white-space: nowrap;
  }
  .divider {
    position: absolute; left: 308px; top: 52px; width: 1px; height: 210px;
    background: linear-gradient(var(--card), var(--divider) 25%, var(--divider) 75%, var(--card));
  }
  .contact {
    position: absolute; left: 332px; top: 64px; color: var(--white);
  }
  .contact-name {
    color: var(--orange); font-weight: 700; font-size: 21px; text-transform: uppercase; letter-spacing: .3px;
  }
  .contact-title { font-size: 17px; font-weight: 500; margin-bottom: 16px; }
  .contact-list { list-style: none; }
  .contact-list li {
    display: flex; align-items: center; gap: 10px;
    font-size: 16px; font-weight: 500; line-height: 1.55;
  }
  .contact-list svg { width: 20px; height: 20px; flex: none; }
  .accent { color: var(--orange); }
  .slogan-band {
    position: absolute; left: 0; right: 0; bottom: 0; height: 72px;
    background: var(--orange);
    display: flex; align-items: center; justify-content: center;
    color: var(--white); font-weight: 700; font-size: 18px; text-transform: uppercase; letter-spacing: .4px;
  }
  /* back */
  .card-back {
    display: flex; flex-direction: column; align-items: center; justify-content: center; gap: 28px;
  }
  .card-back .brand { display: flex; align-items: center; gap: 16px; }
  .card-back .brand-dot { border-color: var(--silver); width: 40px; height: 40px; }
  .card-back .brand-name { color: var(--silver); font-size: 44px; }
  .back-tagline {
    color: var(--white); font-weight: 600; font-size: 18px; text-transform: uppercase; letter-spacing: .3px;
  }
</style>
</head>
<body>
<main class="sheet">
  <section class="card card-front">
    <div class="brand">
      <span class="brand-dot"></span>
      <span class="brand-name">TR Advisory</span>
    </div>
    <div class="divider"></div>
    <div class="contact">
      <p class="contact-name">Dorian Fairweather</p>
      <p class="contact-title">Owner</p>
      <ul class="contact-list">
        <li>
          <svg viewBox="0 0 20 20" aria-hidden="true"><circle cx="10" cy="10" r="9" fill="none" stroke="#ec6a35" stroke-width="1.4"/><path d="M7 5.5l1.6 2.3-1 1.1a7 7 0 003.5 3.5l1.1-1 2.3 1.6-.9 1.5c-3.8-.3-7.3-3.8-7.6-7.6z" fill="#ec6a35"/></svg>
          555-714-3096
        </li>
        <li>
          <svg viewBox="0 0 20 20" aria-hidden="true"><circle cx="10" cy="10" r="9" fill="none" stroke="#ec6a35" stroke-width="1.4"/><rect x="7" y="5" width="6" height="10" rx="1" fill="none" stroke="#ec6a35" stroke-width="1.3"/><circle cx="10" cy="13.2" r=".7" fill="#ec6a35"/></svg>
          555-802-4173
        </li>
        <li>
          <svg viewBox="0 0 20 20" aria-hidden="true"><circle cx="10" cy="10" r="9" fill="#ec6a35"/><rect x="5.5" y="7" width="9" height="6.5" fill="#0b0b0b"/><path d="M5.5 7l4.5 3.5L14.5 7" fill="none" stroke="#ec6a35" stroke-width="1"/></svg>
          d@trvadvisory.example
        </li>
        <li>
          <svg viewBox="0 0 20 20" aria-hidden="true"><circle cx="10" cy="10" r="9" fill="#ec6a35"/><circle cx="10" cy="10" r="5" fill="none" stroke="#0b0b0b" stroke-width="1"/><ellipse cx="10" cy="10" rx="2.2" ry="5" fill="none" stroke="#0b0b0b" stroke-width="1"/><path d="M5 10h10" stroke="#0b0b0b" stroke-width="1"/></svg>
          <span>www.<span class="accent">trvadvisory</span>.example</span>
        </li>
      </ul>
    </div>
    <div class="slogan-band">Connecting you with smarter systems</div>
  </section>

  <section class="card card-back">
    <div class="brand">
      <span class="brand-dot"></span>
      <span class="brand-name">TR Advisory</span>
    </div>
    <p class="back-tagline">Setting the standard in tech</p>
  </section>
</main>
</body>
</html>
```